LanternPips business card for creator of IP TOY (fun) (children) designs

This business card will be the introduction of me as the creator of new designs to the toy industry and beyond. These designs are kept secret until being revealed one on one to each company. My design is patent pending protected IP. I am looking for business appropriate with a tinge of fun. Please no black backgounds as this is the toy industry. Be creative with the logo and colors please. Just imagine.

Target Market(s)

TOY Industry Executives - Inventor Relations - Manufacturers this is my first introduction card.

Industry/Entity Type

Toy Industry - I have included our Brand colors which can be seen on the cover of The Quiet Pebble Moon book so uses for any of these others colors would be intersting.

Contact Information for Business Card

LOGO Mara Delwyn Founder Creator 555 017 2869 4718 E Hollin Bend Fenwick, OK 70812 www.lanternpips-demo.com maradelwyn@quillpost-mail.com Patent Pending IP

Font styles to use
Other font styles liked:
• The font used in the logo is Swiss721BT bold I need to see other fonts to be able to decide but need a clean look

Requirements
Must have
• A bit of an artistic flair although the logo is very simple. I am in the toy industry so would like something that sparks the look of being a creator?
Nice to have
• Please try a background other than stark white. Would like to see a play using brand colors?I like the logos which look like they are lifted off the page. Then under the logo the words (not lifted?) Every Play Every Friend Every Lesson
Should not have
• No Black Backgrounds please! should look as clean as possible - I am not opposed to changing to a double sided card if that is more effectual.

```html
<!DOCTYPE html>
<html lang="en">
<head>
<meta charset="utf-8">
<title>LanternPips Business Card</title>
<link href="https://fonts.googleapis.com/css2?family=Poppins:wght@300;400;600;700&display=swap" rel="stylesheet">
<style>
  :root {
    --page: #e4e4e4;
    --teal: #86cccb;
    --yellow: #f7d93a;
    --sky: #cfe7f3;
    --brand-red: #e4404a;
    --white: #ffffff;
    --toy-yellow: #f4d23c;
    --toy-red: #e8433e;
  }
  * { box-sizing: border-box; margin: 0; padding: 0; }
  html, body { width: 1200px; height: 900px; overflow: hidden; }
  body {
    background: var(--page);
    font-family: "Poppins", sans-serif;
    display: flex;
    align-items: center;
    justify-content: center;
    gap: 40px;
  }
  .card {
    position: relative;
    width: 540px;
    height: 310px;
    border-radius: 22px;
    background: var(--teal);
    overflow: hidden;
    box-shadow: 0 10px 24px rgba(0,0,0,0.12);
  }
  .card-shapes { position: absolute; inset: 0; width: 100%; height: 100%; }
  .card-front .logo-block {
    position: absolute;
    left: 0; right: 0; top: 112px;
    text-align: center;
  }
  .logo-name {
    color: var(--brand-red);
    font-weight: 700;
    font-size: 46px;
    letter-spacing: 0.5px;
    line-height: 1;
  }
  .tagline {
    margin-top: 14px;
    color: var(--white);
    font-size: 13px;
    font-weight: 400;
    letter-spacing: 0.3px;
  }
  .card-back .identity {
    position: absolute;
    left: 34px; top: 30px;
    color: var(--white);
  }
  .person-name { font-weight: 700; font-size: 28px; line-height: 1.1; }
  .person-title { font-weight: 300; font-size: 13px; letter-spacing: 2px; margin-top: 2px; }
  .contact-list {
    position: absolute;
    left: 34px; top: 118px;
    list-style: none;
    color: var(--white);
    font-size: 11.5px;
    font-weight: 300;
    line-height: 1.45;
  }
  .contact-list li { display: flex; align-items: flex-start; gap: 10px; }
  .contact-list svg { width: 11px; height: 11px; margin-top: 3px; flex: none; fill: var(--white); }
  .toy-art {
    position: absolute;
    right: 36px; bottom: 12px;
    width: 190px; height: 122px;
    border-radius: 14px;
    background: linear-gradient(135deg, var(--toy-yellow) 0%, var(--toy-yellow) 55%, var(--toy-red) 100%);
  }
</style>
</head>
<body>

  <section class="card card-front" aria-label="Business card front">
    <svg class="card-shapes" viewBox="0 0 540 310" preserveAspectRatio="none" aria-hidden="true">
      <path d="M0 90 C40 82 70 110 78 150 C86 185 130 190 128 230 C126 262 90 280 60 310 L0 310 Z" fill="var(--yellow)"/>
      <path d="M410 0 C430 40 470 40 480 80 C490 115 520 120 540 130 L540 0 Z" fill="var(--sky)"/>
    </svg>
    <div class="logo-block">
      <div class="logo-name">LanternPips</div>
      <p class="tagline">Every Play Every Friend Every Lesson</p>
    </div>
  </section>

  <section class="card card-back" aria-label="Business card back">
    <svg class="card-shapes" viewBox="0 0 540 310" preserveAspectRatio="none" aria-hidden="true">
      <path d="M410 0 C400 40 440 60 470 70 C505 82 520 110 540 120 L540 0 Z" fill="var(--yellow)"/>
      <path d="M120 310 C130 250 190 232 260 230 C340 228 420 225 470 200 C505 185 525 190 540 200 L540 310 Z" fill="var(--sky)"/>
    </svg>
    <div class="identity">
      <h1 class="person-name">Mara Delwyn</h1>
      <p class="person-title">Founder Creator</p>
    </div>
    <ul class="contact-list">
      <li>
        <svg viewBox="0 0 24 24"><path d="M6.6 10.8a15.1 15.1 0 0 0 6.6 6.6l2.2-2.2c.3-.3.7-.4 1-.2 1.1.4 2.3.6 3.6.6.6 0 1 .4 1 1V20c0 .6-.4 1-1 1A17 17 0 0 1 3 4c0-.6.4-1 1-1h3.5c.6 0 1 .4 1 1 0 1.3.2 2.5.6 3.6.1.3 0 .7-.2 1z"/></svg>
        <span>555 017 2869</span>
      </li>
      <li>
        <svg viewBox="0 0 24 24"><path d="M2 5h20v14H2z M4 7v.5l8 5 8-5V7l-8 5z" fill-rule="evenodd"/></svg>
        <span>maradelwyn@quillpost-mail.com</span>
      </li>
      <li>
        <svg viewBox="0 0 24 24"><path d="M12 2a10 10 0 1 0 0 20 10 10 0 0 0 0-20zm7.9 9h-3.4a15 15 0 0 0-1.3-6A8 8 0 0 1 19.9 11zM12 4c1 1.3 2.2 3.8 2.5 7h-5C9.8 7.8 11 5.3 12 4zM8.8 5a15 15 0 0 0-1.3 6H4.1A8 8 0 0 1 8.8 5zM4.1 13h3.4c.1 2.2.6 4.3 1.3 6a8 8 0 0 1-4.7-6zM12 20c-1-1.3-2.2-3.8-2.5-7h5c-.3 3.2-1.5 5.7-2.5 7zm3.2-1a15 15 0 0 0 1.3-6h3.4a8 8 0 0 1-4.7 6z"/></svg>
        <span>www.lanternpips-demo.com</span>
      </li>
      <li>
        <svg viewBox="0 0 24 24"><path d="M12 2a7 7 0 0 0-7 7c0 5.3 7 13 7 13s7-7.7 7-13a7 7 0 0 0-7-7zm0 9.5A2.5 2.5 0 1 1 12 6.5a2.5 2.5 0 0 1 0 5z"/></svg>
        <span>4718 E Hollin Bend<br>Fenwick, OK 70812</span>
      </li>
    </ul>
    <div class="toy-art" role="img" aria-label="Illustration of colourful toys: a yellow toy bus, a stacking ring tower and a small red toy train"></div>
  </section>

</body>
</html>
```